SnackHarbor!!! A Vending Machine Business Looking for an attractive website.

We are a vending machine business in Northern Michigan. We have changed our name and have rebranded our company. We would like an attractive website that shares who we are, what services we provide, the products we offer in our machines, along with a form businesses can fill out to see if they are a good fit for our company. I would like to have a Home Page, About SnackHarbor, Why Choose SnackHarbor?, Products & Services, Contact Us (With a Login Option), and a page with a questionnaire for thos interested in getting a FREE Vending Machine.

Target Market(s)

Businesses, Campgrounds, Schools, and many more in Northern Michigan

Industry/Entity Type

Vending Machines

Number of Pages Required

5+ page

Requirements
Must have
• An inviting and enticing Home Page. I want to get my potential clients engaged in our website.
Nice to have
• Possibly background photos from Northern Michigan
Should not have
• A corporate feel. I do not want a boring website.

```html
<!DOCTYPE html>
<html lang="en">
<head>
<meta charset="utf-8">
<title>SnackHarbor – Crave. Vend. Repeat</title>
<link href="https://fonts.googleapis.com/css2?family=Outfit:wght@400;500;600&display=swap" rel="stylesheet">
<style>
:root{
  --navy:#23214f;
  --navy-soft:#3a3868;
  --green:#3d5d2b;
  --ink:#1c1c1c;
  --body:#4a4a4a;
  --white:#ffffff;
  --star:#f26a1b;
  --line:#d9d9e3;
}
*{margin:0;padding:0;box-sizing:border-box}
html,body{width:1200px;height:3044px;overflow:hidden}
body{font-family:"Outfit",sans-serif;color:var(--ink);background:var(--white);position:relative}
.abs{position:absolute}
a{color:inherit;text-decoration:none}

.topbar{left:0;top:0;width:1200px;height:40px;background:var(--navy);color:var(--white);font-size:13px;display:flex;align-items:center;justify-content:center}
.topbar b{font-weight:600;margin-left:4px}

.header{left:0;top:40px;width:1200px;height:85px;background:var(--white)}
.brand{left:142px;top:24px;display:flex;align-items:center;gap:8px;font-size:30px;font-weight:600;color:var(--navy)}
.brand i{width:28px;height:28px;border-radius:50%;background:var(--navy);display:block}
.nav{left:453px;top:33px;display:flex;gap:27px;font-size:13.5px}
.nav .active{color:var(--green);font-weight:600}
.btn{display:inline-flex;align-items:center;justify-content:center;background:var(--navy);color:var(--white);font-size:13.5px;border-radius:3px}
.login{left:957px;top:25px;width:101px;height:35px}

.hero{left:0;top:125px;width:1200px;height:529px;background:linear-gradient(100deg,#c9d3de 0%,#b24150 18%,#c23a48 30%,#d9e0e9 50%,#c7d4e3 75%,#dbe3ec 100%)}
.hero-text{right:142px;top:140px;text-align:right}
.hero-text h1{font-size:45px;font-weight:500;line-height:56px}
.hero-text h1 span{color:var(--green)}
.hero-text p{font-size:23px;margin-top:12px}
.hero-text .btn{width:101px;height:35px;margin-top:22px}

.about{left:0;top:654px;width:1200px;height:351px;background:var(--navy);color:var(--white);text-align:center}
.about h2{font-size:31px;font-weight:500;margin-top:77px}
.about p{width:740px;margin:12px auto 0;font-size:13.5px;line-height:22px}
.outline{display:inline-flex;align-items:center;justify-content:center;width:101px;height:35px;border:1px solid var(--white);border-radius:3px;font-size:13.5px;margin-top:24px}

.why-title{left:0;top:1080px;width:1200px;text-align:center;font-size:31px;font-weight:500}
.ring{border:1px solid #ececf2;border-radius:50%}
.icon-circle{width:76px;height:76px;border-radius:50%;background:var(--navy);border:3px solid var(--white);box-shadow:0 0 0 1px var(--navy);display:flex;align-items:center;justify-content:center}
.feature{width:282px;font-size:12.5px;line-height:20.5px;color:var(--body)}
.feature h3{font-size:15.5px;font-weight:500;color:var(--ink);margin-bottom:6px}
.feature b{color:var(--ink);font-weight:600}
.feature.left{text-align:right}
.machine{left:523px;top:1175px;width:156px;height:286px;background:linear-gradient(90deg,#c9ccd1,#eef0f2 40%,#a9adb3);border-radius:4px}
.faint-name{left:776px;top:1505px;font-size:40px;font-weight:600;color:#e6e6ec}

.cta{left:0;top:1639px;width:1200px;height:526px;background:linear-gradient(90deg,#6d7680 0%,#c0392b 30%,#6b7580 45%,#5d6872 100%)}
.cta-text{left:677px;top:1790px;color:var(--white);width:390px}
.cta-text h2{font-size:31px;font-weight:500;line-height:39px}
.cta-text p{font-size:13.5px;line-height:22px;margin-top:14px}
.cta-text .btn{width:101px;height:35px;margin-top:20px}

.testi-title{left:0;top:2240px;width:1200px;text-align:center;font-size:31px;font-weight:500}
.card{width:282px;height:228px;border:1px solid #e4e4ec;border-radius:6px;overflow:hidden;background:var(--white)}
.card p{padding:16px 15px 0;font-size:13px;line-height:21.5px;color:var(--body)}
.card .who{position:absolute;left:0;bottom:0;width:100%;height:60px;background:var(--navy);color:var(--white)}
.avatar{position:absolute;left:14px;top:-18px;width:64px;height:64px;border-radius:50%;background:linear-gradient(#d8dde3,#9aa4b0);border:3px solid var(--white)}
.who .name{position:absolute;left:91px;top:12px;font-size:14px;font-weight:500}
.who .role{position:absolute;left:91px;top:31px;font-size:11.5px;opacity:.85}
.who .stars{position:absolute;right:14px;top:18px;display:flex;gap:3px}
.arrow{width:34px;height:34px;border-radius:50%;background:var(--white);box-shadow:0 2px 8px rgba(0,0,0,.12);display:flex;align-items:center;justify-content:center}

.footer{left:0;top:2663px;width:1200px;height:338px;background:var(--navy);color:var(--white)}
.foot-brand{left:0;top:62px;width:1200px;display:flex;justify-content:center;align-items:center;gap:10px;font-size:40px;font-weight:600}
.foot-brand i{width:36px;height:36px;border-radius:50%;background:var(--white);display:block}
.foot-line{left:142px;width:916px;height:1px;background:#4b4979}
.foot-nav{left:142px;top:184px;width:916px;display:flex;justify-content:space-around;font-size:13.5px}
.foot-nav .active{font-weight:600}
.contact{top:258px;display:flex;align-items:center;gap:14px}
.contact .ci{width:40px;height:40px;border-radius:50%;background:#45436f;display:flex;align-items:center;justify-content:center}
.contact small{display:block;font-size:11.5px;font-weight:600}
.contact span{font-size:14px}
.divider{top:266px;width:1px;height:32px;background:#4b4979}
.bottom{left:0;top:3001px;width:1200px;height:43px;background:var(--green);color:var(--white);font-size:13px}
.bottom .copy{position:absolute;left:142px;top:13px}
.socials{position:absolute;right:142px;top:8px;display:flex;gap:6px}
.socials i{width:28px;height:28px;border-radius:50%;border:1.5px solid var(--white);display:block}
</style>
</head>
<body>

<div class="abs topbar">Lorem Ipsum is simply dummy text of the printing and typesetting industry. – <b>Click Here</b></div>

<header class="abs header">
  <div class="abs brand"><i></i>SnackHarbor</div>
  <nav class="abs nav">
    <a class="active">Home</a><a>About</a><a>Why Choose Us</a><a>Products &amp; Services</a><a>Contact Us</a>
  </nav>
  <a class="abs btn login">Log In</a>
</header>

<section class="abs hero" role="img" aria-label="Bright waiting hall with red snack and drink vending machines beside a blue bench">
  <div class="abs hero-text">
    <h1><span>SnackHarbor</span> :<br>Crave. Vend. Repeat</h1>
    <p>Elevating Snacking, One Vend at a Time</p>
    <a class="btn">Contact Us</a>
  </div>
</section>

<section class="abs about">
  <h2>About SnackHarbor</h2>
  <p>Welcome to SnackHarbor, where snacking meets delight! We're not just about vending machines;we're your culinary companions, your flavor curators, and your secret stash of happiness. Mark and Elena, the dynamic duo behind SnackHarbor, have a passion for all things tasty. With backgrounds in sales and a penchant for personal connections, they've transformed the vending experience into an art form.</p>
  <a class="outline">Read More</a>
</section>

<h2 class="abs why-title">Why Choose SnackHarbor?</h2>
<div class="abs ring" style="left:396px;top:1136px;width:362px;height:362px"></div>
<div class="abs machine" role="img" aria-label="Stainless steel snack vending machine stocked with chips and candy"></div>

<div class="abs icon-circle" style="left:437px;top:1141px">
  <svg width="34" height="34" viewBox="0 0 24 24" fill="none" stroke="#fff" stroke-width="1.4"><path d="M12 21s-6-5.5-6-10a6 6 0 0 1 12 0c0 4.5-6 10-6 10z"/><path d="M12 13.5l-2.6-2.5a1.6 1.6 0 0 1 2.6-1.9 1.6 1.6 0 0 1 2.6 1.9z"/></svg>
</div>
<div class="abs icon-circle" style="left:687px;top:1141px">
  <svg width="34" height="34" viewBox="0 0 24 24" fill="none" stroke="#fff" stroke-width="1.4"><path d="M7 21v-8l4-6c1 0 1.5 1 1 2l-1 3h6c1 0 1.6 1 1.3 2l-1.5 5c-.3.8-1 1.2-1.8 1.2z"/><path d="M4 13h3v8H4z"/></svg>
</div>
<div class="abs icon-circle" style="left:437px;top:1384px">
  <svg width="34" height="34" viewBox="0 0 24 24" fill="none" stroke="#fff" stroke-width="1.4"><circle cx="9" cy="8" r="4"/><circle cx="15" cy="15" r="5"/><path d="M13 15h.01M17 15h.01M13.5 17.5c1 .8 2 .8 3 0"/></svg>
</div>
<div class="abs icon-circle" style="left:687px;top:1384px">
  <svg width="34" height="34" viewBox="0 0 24 24" fill="none" stroke="#fff" stroke-width="1.4"><path d="M4 20h16M6 20v-5h3v5M11 20v-8h3v8M16 20v-11h3v11M5 11l5-4 3 2 6-5"/></svg>
</div>

<div class="abs feature left" style="left:142px;top:1146px">
  <h3>1. Local Love</h3>
  We celebrate the heart of Michigan by partnering with local legends. Say hello to <b>Pine Ridge Jerky and Lakeshore Kettle Chips</b>—our hometown heroes. Their flavors dance on your taste buds, and we're thrilled to bring them straight to your workplace.
</div>
<div class="abs feature left" style="left:142px;top:1389px">
  <h3>2. Unleash Your Cravings</h3>
  SnackHarbor isn't bound by corporate ties. We're the rebels of the vending world. Craving a bag of crispy, kettle-cooked chips? Done. Hankering for jerky that packs a punch? We've got you covered. Our machines are like treasure chests, waiting for you to unlock flavor magic.
</div>
<div class="abs feature" style="left:775px;top:1146px">
  <h3>3. Quality Meets Convenience</h3>
  Imagine this: You're mid-meeting, and your stomach growls. Fear not! SnackHarbor's machines offer top-notch snacks and beverages. It's like having a mini food festival at your fingertips.<br>
  <b>Tap to Pay</b> : No fumbling for change! SnackHarbor accepts tap-to-pay options, credit cards, and even Orchard Pay and Glide Pay. Seamless snacking, guaranteed.
</div>
<div class="abs feature" style="left:775px;top:1389px">
  <h3>4. Pandemic-Proof &amp; Recession-Ready</h3>
  Life throws curveballs, but SnackHarbor stands strong. Our vending machines are the unsung heroes of resilience. Rain or shine, they're there, serving up joy.
</div>
<div class="abs faint-name">SnackHarbor</div>

<section class="abs cta" role="img" aria-label="Black snack machine and red cold drink machine standing against a grey wall">
</section>
<div class="abs cta-text">
  <h2>Ready to experience the SnackHarbor difference?</h2>
  <p>Sign up now and let's connect. Taste the future of snacking firsthand! Contact us today and explore how our vending magic can elevate your space.</p>
  <a class="btn">Contact Us</a>
</div>

<h2 class="abs testi-title">Customer Testimonials</h2>

<div class="abs arrow" style="left:90px;top:2425px">
  <svg width="16" height="10" viewBox="0 0 16 10" fill="none" stroke="#bbb" stroke-width="1.2"><path d="M15 5H1M5 1L1 5l4 4"/></svg>
</div>
<div class="abs arrow" style="left:1073px;top:2425px">
  <svg width="16" height="10" viewBox="0 0 16 10" fill="none" stroke="#222" stroke-width="1.2"><path d="M1 5h14M11 1l4 4-4 4"/></svg>
</div>

<div class="abs card" style="left:142px;top:2350px">
  <p>Lorem ipsum dolor sit amet, amet ut ea consectetur adipiscing elit, sed do ex eiusmod tempor incididunt ut labore et dolore magna aliqua. Ut enim ad dolor minim veniam, quis nostrud amet ut ua exercitation.</p>
  <div class="who"><div class="avatar" role="img" aria-label="Customer portrait"></div><div class="name">Owen Hale</div><div class="role">Lorem Ipsum</div>
    <div class="stars"><svg width="66" height="11" viewBox="0 0 66 11" fill="#f26a1b"><path id="s" d="M5.5 0l1.6 3.5 3.9.4-2.9 2.6.8 3.8-3.4-2-3.4 2 .8-3.8L0 3.9l3.9-.4z"/><use href="#s" x="14"/><use href="#s" x="28"/><use href="#s" x="42"/><use href="#s" x="55"/></svg></div></div>
</div>
<div class="abs card" style="left:467px;top:2298px">
  <p>Lorem ipsum dolor sit amet, amet ut ea consectetur adipiscing elit, sed do ex eiusmod tempor incididunt ut labore et dolore magna aliqua. Ut enim ad dolor minim veniam, quis nostrud amet ut ua exercitation.</p>
  <div class="who"><div class="avatar" role="img" aria-label="Customer portrait"></div><div class="name">Clara Benton</div><div class="role">Lorem Ipsum</div>
    <div class="stars"><svg width="66" height="11" viewBox="0 0 66 11" fill="#f26a1b"><use href="#s"/><use href="#s" x="14"/><use href="#s" x="28"/><use href="#s" x="42"/><use href="#s" x="55"/></svg></div></div>
</div>
<div class="abs card" style="left:776px;top:2350px">
  <p>Lorem ipsum dolor sit amet, amet ut ea consectetur adipiscing elit, sed do ex eiusmod tempor incididunt ut labore et dolore magna aliqua. Ut enim ad dolor minim veniam, quis nostrud amet ut ua exercitation.</p>
  <div class="who"><div class="avatar" role="img" aria-label="Customer portrait"></div><div class="name">Miles Foster</div><div class="role">Lorem Ipsum</div>
    <div class="stars"><svg width="66" height="11" viewBox="0 0 66 11" fill="#f26a1b"><use href="#s"/><use href="#s" x="14"/><use href="#s" x="28"/><use href="#s" x="42"/><use href="#s" x="55"/></svg></div></div>
</div>

<footer class="abs footer">
  <div class="abs foot-brand"><i></i>SnackHarbor</div>
  <div class="abs foot-line" style="top:169px"></div>
  <nav class="abs foot-nav"><a class="active">Home</a><a>About</a><a>Why Choose Us</a><a>Products &amp; Services</a><a>Contact Us</a></nav>
  <div class="abs foot-line" style="top:226px"></div>

  <div class="abs contact" style="left:202px">
    <div class="ci"><svg width="18" height="14" viewBox="0 0 18 14" fill="none" stroke="#fff" stroke-width="1.4"><rect x="1" y="1" width="16" height="12" rx="1"/><path d="M1 2l8 6 8-6"/></svg></div>
    <div><small>Email</small><span>info@snackharbor.com</span></div>
  </div>
  <div class="abs divider" style="left:422px"></div>
  <div class="abs contact" style="left:492px">
    <div class="ci"><svg width="14" height="18" viewBox="0 0 14 18" fill="none" stroke="#fff" stroke-width="1.4"><path d="M7 17s-6-6-6-10a6 6 0 0 1 12 0c0 4-6 10-6 10z"/><circle cx="7" cy="7" r="2"/></svg></div>
    <div><span style="font-size:13.5px;line-height:17px;display:block">123, Building Name,<br>Street City, State XY 1234</span></div>
  </div>
  <div class="abs divider" style="left:782px"></div>
  <div class="abs contact" style="left:851px">
    <div class="ci"><svg width="18" height="18" viewBox="0 0 24 24" fill="none" stroke="#fff" stroke-width="1.6"><path d="M22 16.9v3a2 2 0 0 1-2.2 2A19.8 19.8 0 0 1 2.1 4.2 2 2 0 0 1 4.1 2h3a2 2 0 0 1 2 1.7c.1 1 .4 1.9.7 2.8a2 2 0 0 1-.5 2.1L8 9.9a16 16 0 0 0 6 6l1.3-1.3a2 2 0 0 1 2.1-.4c.9.3 1.8.6 2.8.7a2 2 0 0 1 1.7 2z"/></svg></div>
    <div><small>Phone</small><span style="font-size:15px">123-456-7890</span></div>
  </div>
</footer>

<div class="abs bottom">
  <span class="copy">© 2024 SnackHarbor. All Rights Reserved.</span>
  <div class="socials"><i></i><i></i><i></i><i></i></div>
</div>

</body>
</html>
```